Fashion Design Business Card

I need a new business card designed for a new fashion company. I have attached what I have currently designed. I want it more feminine looking, the logo needs to be gold. I want it simple, feminine and stylish. Please give me some different ideas with the fonts.
Updates

I need to send the design we currently have, as we have worked out the logo.
You also need all of our details
Industry/Entity Type
Fashion
Look and feel
Each slider illustrates characteristics of the customer's brand and the style your logo design should communicate.

```html
<!DOCTYPE html>
<html lang="en">
<head>
<meta charset="utf-8">
<title>Marina Holloway – Business Card</title>
<link rel="stylesheet" href="https://fonts.googleapis.com/css2?family=Cinzel:wght@400;500&family=Arimo:wght@400&display=swap">
<style>
  :root {
    --stage: #e8e3db;
    --card-white: #ffffff;
    --band-brown: #4a3a2c;
    --gold: #e0a800;
    --text-light: #f3ede4;
    --back-dark: #1c130b;
    --back-glow: #5a4a3b;
  }
  * { margin: 0; padding: 0; box-sizing: border-box; }
  html, body {
    width: 1200px;
    height: 900px;
    overflow: hidden;
    background: var(--stage);
  }
  .card {
    position: absolute;
    left: 266px;
    width: 674px;
    height: 380px;
    box-shadow: 0 2px 8px rgba(0, 0, 0, 0.18);
    overflow: hidden;
  }
  .card-front {
    top: 50px;
    background: var(--card-white);
  }
  .card-back {
    top: 476px;
    height: 382px;
    background: radial-gradient(ellipse 60% 70% at 50% 22%, var(--back-glow) 0%, #3a2c1f 40%, var(--back-dark) 100%);
  }
  .identity-band {
    position: absolute;
    left: 0;
    top: 116px;
    width: 300px;
    height: 148px;
    background: var(--band-brown);
    padding: 32px 0 0 44px;
    color: var(--text-light);
  }
  .person-name {
    font-family: "Cinzel", serif;
    font-weight: 400;
    font-size: 21px;
    letter-spacing: 0.5px;
    color: var(--gold);
    line-height: 1;
  }
  .person-role {
    font-family: "Cinzel", serif;
    font-size: 13px;
    letter-spacing: 0.3px;
    margin-top: 7px;
    line-height: 1;
  }
  .contact-list {
    list-style: none;
    margin-top: 20px;
    font-family: "Arimo", sans-serif;
    font-size: 10px;
    line-height: 15px;
  }
  .contact-list .label { display: inline-block; width: 14px; }
  .brand-mark {
    position: absolute;
    display: flex;
    align-items: center;
    gap: 14px;
    font-family: "Cinzel", serif;
    font-weight: 400;
    color: var(--gold);
    white-space: nowrap;
  }
  .brand-mark .dot {
    display: block;
    border-radius: 50%;
    background: var(--gold);
  }
  .card-front .brand-mark {
    right: 30px;
    top: 168px;
    font-size: 30px;
    letter-spacing: 1px;
  }
  .card-front .brand-mark .dot { width: 22px; height: 22px; }
  .card-back .brand-mark {
    left: 50%;
    top: 122px;
    transform: translateX(-50%);
    font-size: 26px;
    letter-spacing: 1px;
  }
  .card-back .brand-mark .dot { width: 18px; height: 18px; }
  .back-name {
    position: absolute;
    left: 0;
    right: 0;
    top: 266px;
    text-align: center;
    font-family: "Cinzel", serif;
    font-size: 25px;
    letter-spacing: 1px;
    color: var(--gold);
  }
</style>
</head>
<body>
  <section class="card card-front">
    <div class="identity-band">
      <h1 class="person-name">MARINA HOLLOWAY</h1>
      <p class="person-role">FASHION DESIGNER</p>
      <ul class="contact-list">
        <li><span class="label">P :</span>0400612734</li>
        <li><span class="label">E :</span>marina@marinaholloway.com</li>
        <li>www.marinaholloway.com</li>
      </ul>
    </div>
    <div class="brand-mark"><span class="dot"></span>MARINA HOLLOWAY</div>
  </section>

  <section class="card card-back">
    <div class="brand-mark"><span class="dot"></span>MARINA HOLLOWAY</div>
    <p class="back-name">MARINA HOLLOWAY</p>
  </section>
</body>
</html>
```